Family owned plumbing contractor needs eye catching business card design

Business cards that are unique, eye catching, and provide customers with general company information, such as name, address, phone number, website, employee name/title, cell phone #, & email address. We are transitioning to a new logo that utilizes a more retro feel, so we are interested in seeing some cool old school designs in the mix. We are liking the dark background on some of the samples on this website. If that is workable with our artwork, we would like to see that incorporated into the design.
Contact Information for Business Card
Copperline Pipeworks, Inc.
www.copperlinepipeworks.example
(555) 392-7068 phone
Nevada License #64205
California License #5810473
Dale Wrennick, President
(555) 618-9032 cell
dale@copperlinepipeworks.example
Residential * Commercial * Service
Requirements
Must have
- The business card details listed above & logo provided.
Nice to have
- I made some notes about color options in the description.

```html
<!DOCTYPE html>
<html lang="en">
<head>
<meta charset="utf-8">
<title>Copperline Pipeworks – Business Cards</title>
<link href="https://fonts.googleapis.com/css2?family=Jost:wght@400;500&family=Alice&display=swap" rel="stylesheet">
<style>
  :root {
    --backdrop: #2c2d2f;
    --card: #38393b;
    --teal: #84d9c6;
    --grey: #a7a8aa;
    --white: #f2f2f2;
  }
  * { margin: 0; padding: 0; box-sizing: border-box; }
  html, body { width: 1200px; height: 1000px; overflow: hidden; }
  body {
    background: var(--backdrop);
    font-family: "Jost", sans-serif;
    position: relative;
  }
  .card {
    position: absolute;
    left: 250px;
    width: 700px;
    height: 400px;
    background: var(--card);
    border-radius: 24px;
  }
  .card-front { top: 60px; }
  .card-back { top: 540px; }

  .brand {
    display: flex;
    align-items: center;
    gap: 14px;
    color: var(--teal);
    font-weight: 500;
  }
  .brand-dot {
    width: 22px; height: 22px;
    border-radius: 50%;
    background: var(--teal);
    flex: none;
  }
  .card-front .brand {
    position: absolute;
    top: 140px; left: 0; right: 0;
    justify-content: center;
    font-size: 38px;
  }
  .tagline {
    position: absolute;
    left: 0; right: 0; top: 300px;
    text-align: center;
    color: var(--teal);
    font-size: 17px;
    letter-spacing: 2.5px;
  }

  .card-back .brand {
    position: absolute;
    top: 72px; left: 50px;
    font-size: 22px;
  }
  .contact {
    position: absolute;
    left: 330px; top: 120px; right: 0;
  }
  .person-name {
    font-family: "Alice", serif;
    color: var(--teal);
    font-size: 28px;
    line-height: 1;
  }
  .person-title {
    color: var(--white);
    font-size: 13px;
    font-weight: 500;
    margin-top: 4px;
  }
  .rule {
    height: 1px;
    background: var(--teal);
    margin: 16px 0 22px;
  }
  .company {
    color: var(--teal);
    font-size: 18px;
    margin-bottom: 6px;
  }
  .contact-list { list-style: none; }
  .contact-list li {
    display: flex;
    align-items: center;
    gap: 10px;
    color: var(--grey);
    font-size: 16px;
    line-height: 26px;
  }
  .contact-list svg { width: 14px; height: 14px; fill: var(--grey); flex: none; }
  .licenses {
    color: var(--teal);
    font-size: 15px;
    line-height: 22px;
    margin-top: 4px;
  }
</style>
</head>
<body>
  <section class="card card-front">
    <div class="brand"><span class="brand-dot"></span>Copperline Pipeworks, Inc.</div>
    <p class="tagline">RESIDENTIAL • COMMERCIAL • SERVICE</p>
  </section>

  <section class="card card-back">
    <div class="brand"><span class="brand-dot"></span>Copperline Pipeworks, Inc.</div>
    <div class="contact">
      <p class="person-name">Dale Wrennick</p>
      <p class="person-title">President</p>
      <div class="rule"></div>
      <p class="company">Copperline Pipeworks, Inc.</p>
      <ul class="contact-list">
        <li><svg viewBox="0 0 24 24"><path d="M6.6 10.8a15 15 0 0 0 6.6 6.6l2.2-2.2a1 1 0 0 1 1-.25 11.4 11.4 0 0 0 3.6.57 1 1 0 0 1 1 1V20a1 1 0 0 1-1 1A17 17 0 0 1 3 4a1 1 0 0 1 1-1h3.5a1 1 0 0 1 1 1c0 1.25.2 2.45.57 3.57a1 1 0 0 1-.25 1z"/></svg>(555) 392-7068</li>
        <li><svg viewBox="0 0 24 24"><path d="M7 1h10a2 2 0 0 1 2 2v18a2 2 0 0 1-2 2H7a2 2 0 0 1-2-2V3a2 2 0 0 1 2-2zm0 3v15h10V4zm5 16.2a1 1 0 1 0 0 .01z"/></svg>(555) 618-9032</li>
        <li><svg viewBox="0 0 24 24"><path d="M2 5h20v14H2zm2 2v.5l8 5 8-5V7zm0 2.8V17h16V9.8l-8 5z"/></svg>dale@copperlinepipeworks.example</li>
        <li><svg viewBox="0 0 24 24"><path d="M12 2a10 10 0 1 0 0 20 10 10 0 0 0 0-20zm6.9 6h-2.9a15 15 0 0 0-1.4-3.6A8 8 0 0 1 18.9 8zM12 4a13 13 0 0 1 1.9 4h-3.8A13 13 0 0 1 12 4zM4.3 14a8 8 0 0 1 0-4h3.4a16 16 0 0 0 0 4zm.8 2h2.9a15 15 0 0 0 1.4 3.6A8 8 0 0 1 5.1 16zM8 8H5.1a8 8 0 0 1 4.3-3.6A15 15 0 0 0 8 8zm4 12a13 13 0 0 1-1.9-4h3.8A13 13 0 0 1 12 20zm2.3-6H9.7a14 14 0 0 1 0-4h4.6a14 14 0 0 1 0 4zm.3 5.6A15 15 0 0 0 16 16h2.9a8 8 0 0 1-4.3 3.6zM16.3 14a16 16 0 0 0 0-4h3.4a8 8 0 0 1 0 4z"/></svg>www.copperlinepipeworks.example</li>
      </ul>
      <p class="licenses">Nevada License #64205<br>California License #5810473</p>
    </div>
  </section>
</body>
</html>
```